Need a plumber

Would like a postcard sized flyer made up. Want the design to be kept very simple.
List of services we carry out in bullet point or similar.
Phone number and email included on the flyer.
Logo to feature prominantly.

List of services: Hot water issues
Burst Pipes
Gas Plumbing
Roof leaks
Drain blockages

Target Market(s)

Mums, dads and hosehgold owners

Industry/Entity Type

Plumbing

Colors
0054AA
0677BA
7BADD7
CADEEF
E8F1F8

Requirements
Must have
• Services we off and our logo, also must say "local plumber"

```html
<!DOCTYPE html>
<html lang="en">
<head>
<meta charset="utf-8">
<title>Clear Flow Postcard</title>
<link href="https://fonts.googleapis.com/css2?family=Kaushan+Script&family=Poppins:wght@400;500;600;800&display=swap" rel="stylesheet">
<style>
  :root{
    --blue-deep:#0054AA;
    --blue-mid:#0677BA;
    --blue-soft:#7BADD7;
    --blue-pale:#CADEEF;
    --blue-mist:#E8F1F8;
    --ink:#2a2a2a;
    --backdrop:#8f8f8f;
    --white:#ffffff;
  }
  *{margin:0;padding:0;box-sizing:border-box}
  html,body{width:1200px;height:1200px;overflow:hidden;background:var(--backdrop);font-family:"Poppins",sans-serif}
  .postcard{position:absolute;left:165px;top:284px;width:871px;height:631px;overflow:hidden;background:var(--white)}
  .photo-area{position:absolute;inset:0;background:linear-gradient(160deg,#e9e6e1 0%,#cfc9c1 35%,#8f8a85 60%,#3f5fb5 80%,#c9c6c2 100%)}
  .shapes{position:absolute;inset:0}
  .brand-plate{position:absolute;left:169px;top:32px;width:186px;height:186px;border-radius:50%;background:var(--white);display:flex;align-items:center;justify-content:center}
  .brand-name{font-weight:600;color:var(--ink);font-size:24px;line-height:1;letter-spacing:3px;text-transform:uppercase;white-space:nowrap}
  .headline{position:absolute;left:0;width:520px;text-align:center}
  .headline-script{top:222px;font-family:"Kaushan Script",cursive;color:var(--blue-soft);font-size:58px;line-height:1;padding-left:10px}
  .headline-main{top:282px;font-weight:800;font-size:72px;line-height:1;letter-spacing:-1px;background:linear-gradient(90deg,var(--blue-deep),var(--blue-mid));-webkit-background-clip:text;background-clip:text;color:transparent}
  .headline-sub{top:350px;font-weight:500;font-size:32px;line-height:1;color:var(--blue-deep)}
  .services-title{position:absolute;top:412px;left:160px;width:212px;display:flex;align-items:center;gap:6px;font-weight:800;font-size:19px;color:var(--ink);white-space:nowrap}
  .services-title::before,.services-title::after{content:"";flex:1;height:2px;background:var(--blue-deep)}
  .service{position:absolute;top:448px;width:90px;margin-left:-45px;text-align:center}
  .service-icon{width:61px;height:61px;margin:0 auto;border-radius:50%;background:var(--blue-deep);display:flex;align-items:center;justify-content:center}
  .service-label{margin-top:3px;font-size:14px;line-height:16.5px;color:var(--ink)}
  .contact-strip{position:absolute;left:0;top:578px;width:540px;height:31px;border-top:1px solid var(--blue-mid);border-bottom:1px solid var(--blue-mid);display:flex;align-items:center;gap:16px;padding-left:51px;font-size:15px;color:var(--ink)}
  .contact-item{display:flex;align-items:center;gap:7px}
  .call-box{position:absolute;left:577px;top:556px;color:var(--white);display:flex;align-items:center;gap:8px}
  .call-text{line-height:1}
  .call-label{font-weight:800;font-size:17px}
  .call-number{font-weight:800;font-size:28px;margin-top:4px;letter-spacing:-0.3px}
</style>
</head>
<body>
<div class="postcard">
  <div class="photo-area" role="img" aria-label="Photo of a smiling plumber in blue overalls fitting a drain hose under a kitchen sink"></div>

  <svg class="shapes" width="871" height="631" viewBox="0 0 871 631">
    <defs>
      <linearGradient id="bandBlue" x1="0" y1="0" x2="1" y2="0">
        <stop offset="0" stop-color="#0054AA"/><stop offset="1" stop-color="#0677BA"/>
      </linearGradient>
    </defs>
    <path d="M0 0 H330 C380 120 470 180 477 330 V400 C540 430 590 480 612 540 L612 631 H0 Z" fill="#f4f6f9"/>
    <path d="M0 0 H422 C360 60 280 100 170 118 C100 126 40 125 0 122 Z" fill="url(#bandBlue)"/>
    <path d="M498 631 C530 580 570 545 650 528 C740 512 820 512 871 520 V631 Z" fill="url(#bandBlue)"/>
  </svg>

  <div class="brand-plate">
    <span class="brand-name">Clear Flow</span>
  </div>

  <div class="headline headline-script">Ultimate</div>
  <div class="headline headline-main">Plumbing</div>
  <div class="headline headline-sub">solution expert</div>

  <div class="services-title">OUR SERVICES</div>

  <div class="service" style="left:93px">
    <div class="service-icon"><svg width="36" height="36" viewBox="0 0 36 36" fill="none" stroke="#fff" stroke-width="2" stroke-linecap="round"><path d="M4 20c4-3 8 3 14 0s10 3 14 0M4 26c4-3 8 3 14 0s10 3 14 0M4 32c4-3 8 3 14 0s10 3 14 0M10 14c-2-3 2-5 0-9M18 14c-2-3 2-5 0-9M26 14c-2-3 2-5 0-9"/></svg></div>
    <div class="service-label">Hot water<br>issues</div>
  </div>
  <div class="service" style="left:178px">
    <div class="service-icon"><svg width="38" height="36" viewBox="0 0 38 36" fill="none" stroke="#fff" stroke-width="2" stroke-linejoin="round"><path d="M3 8h13l-2 4 2 4H3zM35 8H22l2 4-2 4h13z"/><path d="M19 22c-3 4-3 6 0 7 3-1 3-3 0-7z"/></svg></div>
    <div class="service-label">Burst Pipes</div>
  </div>
  <div class="service" style="left:263px">
    <div class="service-icon"><svg width="36" height="36" viewBox="0 0 36 36" fill="none" stroke="#fff" stroke-width="2" stroke-linejoin="round"><circle cx="18" cy="6" r="3"/><path d="M4 14h28M8 14v18M28 14v18M18 9v5"/><path d="M18 32c-5 0-6-5-2-9 0 3 2 3 2 1 3 2 5 8 0 8z"/></svg></div>
    <div class="service-label">Gas<br>Plumbing</div>
  </div>
  <div class="service" style="left:348px">
    <div class="service-icon"><svg width="36" height="36" viewBox="0 0 36 36" fill="none" stroke="#fff" stroke-width="2" stroke-linejoin="round"><path d="M3 14h22v5H3zM20 19h8v14h-4V23h-4z"/><path d="M12 4c-2 3-2 5 0 5s2-2 0-5zM20 4c-2 3-2 5 0 5s2-2 0-5z"/></svg></div>
    <div class="service-label">Roof leaks</div>
  </div>
  <div class="service" style="left:433px">
    <div class="service-icon"><svg width="36" height="36" viewBox="0 0 36 36" fill="none" stroke="#fff" stroke-width="2.2" stroke-linecap="round"><path d="M7 14v8a6 6 0 0 0 12 0V10a5 5 0 0 1 10 0v6M4 14h6M26 16h6"/></svg></div>
    <div class="service-label">Drain<br>blockages</div>
  </div>

  <div class="contact-strip">
    <span class="contact-item"><svg width="14" height="11" viewBox="0 0 14 11" fill="none" stroke="#0677BA" stroke-width="1"><rect x="0.5" y="0.5" width="13" height="10"/><path d="M0.5 0.5 7 6l6.5-5.5"/></svg>dan@clearflowplumb.com</span>
    <span class="contact-item"><svg width="14" height="14" viewBox="0 0 14 14" fill="none" stroke="#0677BA" stroke-width="1"><circle cx="7" cy="7" r="6.3"/><ellipse cx="7" cy="7" rx="3" ry="6.3"/><path d="M0.7 7h12.6M1.8 3.8h10.4M1.8 10.2h10.4"/></svg>www.clearflowplumb.com</span>
  </div>

  <div class="call-box">
    <svg width="52" height="52" viewBox="0 0 52 52" fill="none" stroke="#fff" stroke-width="2.4" stroke-linecap="round" stroke-linejoin="round"><path d="M10 8l7-2 5 11-5 4c2 6 6 10 12 13l4-5 11 5-2 7c-18 1-33-15-32-33z"/><path d="M30 10a12 12 0 0 1 11 11M30 3a19 19 0 0 1 18 18"/></svg>
    <div class="call-text">
      <div class="call-label">CALL US TODAY!</div>
      <div class="call-number">+61 400 555 012</div>
    </div>
  </div>
</div>
</body>
</html>
```